23rd Annual Bramblecove Maverick Film Festival Poster

Design an eye catchy, stylish poster for our 23rd film festival. Be different not just a poster with a film reel. Think outside of the box with a design that will attract peoples attention. Colorful (you choose the colors). Make it fun and creative, like the film festival. Show your talents in the design. Be sure it is new and stylish. Dates are August 21 - 29, 2020. Poster size will be 27 inches by 40 inches

Target Market(s)

Upper Middle class - movie lovers

Font styles to use
Sans Serif

Colors
33a6d7

Requirements
Must have
• NO CLIP ART - be original !
Nice to have
• abstract - think outside the box
Should not have
• CLIP ART

```html
<!DOCTYPE html>
<html lang="en">
<head>
<meta charset="utf-8">
<title>23rd Annual Bramblecove Maverick Film Festival 2020</title>
<link rel="stylesheet" href="https://fonts.googleapis.com/css2?family=Titan+One&display=swap">
<style>
  :root {
    --night: #3a3148;
    --indigo: #34306e;
    --ember: #a8302a;
    --lagoon: #1f4b4c;
    --plum: #4a2a5e;
    --outline: #d9d5e8;
    --ink: #2a1f24;
    --paper: #f4f2f4;
    --moon-light: #e6e0ee;
    --moon-violet: #7a4fa8;
  }
  html, body {
    margin: 0;
    padding: 0;
    overflow: hidden;
    background: var(--night);
  }
  .poster {
    position: relative;
    width: 810px;
    height: 1200px;
    overflow: hidden;
    background: var(--night);
    font-family: "Titan One", sans-serif;
  }
  .poster svg {
    position: absolute;
    inset: 0;
    display: block;
  }
  .title-outline {
    fill: none;
    stroke: var(--outline);
    stroke-width: 1.4;
    font-family: "Titan One", sans-serif;
  }
  .year-shadow {
    fill: none;
    stroke: var(--ink);
    stroke-width: 9;
    stroke-linejoin: round;
    font-family: "Titan One", sans-serif;
  }
  .year {
    fill: #3c3040;
    stroke: var(--outline);
    stroke-width: 1.4;
    font-family: "Titan One", sans-serif;
  }
  .dates {
    fill: var(--paper);
    font-family: "Titan One", sans-serif;
  }
</style>
</head>
<body>
<main class="poster">
  <svg width="810" height="1200" viewBox="0 0 810 1200" xmlns="http://www.w3.org/2000/svg">
    <defs>
      <radialGradient id="ember-wash" cx="0.5" cy="0.5" r="0.5">
        <stop offset="0" stop-color="var(--ember)" stop-opacity="0.95"/>
        <stop offset="0.7" stop-color="var(--ember)" stop-opacity="0.7"/>
        <stop offset="1" stop-color="var(--ember)" stop-opacity="0"/>
      </radialGradient>
      <radialGradient id="lagoon-wash" cx="0.5" cy="0.5" r="0.5">
        <stop offset="0" stop-color="var(--lagoon)" stop-opacity="0.95"/>
        <stop offset="0.75" stop-color="var(--lagoon)" stop-opacity="0.7"/>
        <stop offset="1" stop-color="var(--lagoon)" stop-opacity="0"/>
      </radialGradient>
      <radialGradient id="indigo-wash" cx="0.5" cy="0.5" r="0.5">
        <stop offset="0" stop-color="var(--indigo)" stop-opacity="0.9"/>
        <stop offset="1" stop-color="var(--indigo)" stop-opacity="0"/>
      </radialGradient>
      <radialGradient id="plum-wash" cx="0.5" cy="0.5" r="0.5">
        <stop offset="0" stop-color="var(--plum)" stop-opacity="0.9"/>
        <stop offset="1" stop-color="var(--plum)" stop-opacity="0"/>
      </radialGradient>
      <radialGradient id="moon-fill" cx="0.62" cy="0.55" r="0.6">
        <stop offset="0" stop-color="var(--moon-violet)"/>
        <stop offset="0.45" stop-color="#9a86b8"/>
        <stop offset="0.8" stop-color="var(--moon-light)"/>
        <stop offset="1" stop-color="#c9c0d8"/>
      </radialGradient>
    </defs>

    <g class="backdrop" role="img" aria-label="Abstract painted background of indigo, red and teal washes">
      <rect width="810" height="1200" fill="var(--night)"/>
      <ellipse cx="120" cy="220" rx="330" ry="320" fill="url(#indigo-wash)"/>
      <ellipse cx="470" cy="160" rx="200" ry="260" fill="url(#ember-wash)"/>
      <ellipse cx="720" cy="360" rx="230" ry="240" fill="url(#lagoon-wash)"/>
      <ellipse cx="720" cy="1000" rx="220" ry="320" fill="url(#plum-wash)"/>
      <ellipse cx="80" cy="1000" rx="180" ry="260" fill="url(#indigo-wash)" opacity="0.5"/>
    </g>

    <g class="moon-portrait" role="img" aria-label="Painted moon with a dreamy violet portrait face drawn across it">
      <ellipse cx="397" cy="795" rx="325" ry="318" fill="url(#moon-fill)"/>
    </g>

    <g class="festival-title">
      <text class="title-outline" x="146" y="181" font-size="128" textLength="172" lengthAdjust="spacingAndGlyphs">23</text>
      <text class="title-outline" x="326" y="181" font-size="72" textLength="446" lengthAdjust="spacingAndGlyphs">rd ANNUAL</text>
      <text class="title-outline" x="30" y="286" font-size="112" textLength="750" lengthAdjust="spacingAndGlyphs">BRAMBLECOVE</text>
      <text class="title-outline" x="49" y="372" font-size="78" textLength="707" lengthAdjust="spacingAndGlyphs">Maverick Film</text>
      <text class="year-shadow" x="92" y="462" font-size="84" textLength="248" lengthAdjust="spacingAndGlyphs">2020</text>
      <text class="year" x="92" y="462" font-size="84" textLength="248" lengthAdjust="spacingAndGlyphs">2020</text>
      <text class="title-outline" x="416" y="458" font-size="68" textLength="351" lengthAdjust="spacingAndGlyphs">FESTIVAL</text>
    </g>

    <text class="dates" x="186" y="1142" font-size="60" textLength="462" lengthAdjust="spacingAndGlyphs">August 21 - 29</text>
  </svg>
</main>
</body>
</html>
```